Marigold Shore Realty business card design

Looking for an upscale and clean business card design and updated logo. I sell to a very high-end south Florida real estate market.
Target Market(s)
High-end real estate in south Florida real estate market
Industry/Entity Type
Real Estate Agent
Contact Information for Business Card
Marigold Shore Realty, Inc
738 West Penrick Ave, Suite 400/500, Fort Lauderdale, FL 33315
Tim Harlow - Broker/Owner
954-327-8846 Direct
timshomes@quillmail.net
Website: StayPenrickAv.net
Font styles to use
Other font styles liked:
- Copperplate Gothic, Georgia, etc.
Requirements
Must have
- My photo, company name, my name and title, all info stated in Details above
Nice to have
- Luxury home design element, waterfront

```html
<!DOCTYPE html>
<html lang="en">
<head>
<meta charset="utf-8">
<title>Marigold Shore Realty – Business Card</title>
<link href="https://fonts.googleapis.com/css2?family=Cinzel:wght@400&family=Gelasio:wght@400;700&display=swap" rel="stylesheet">
<style>
  :root {
    --page: #fdfdfd;
    --brand-blue: #234a8f;
    --deep-navy: #2b2950;
    --sun-yellow: #ffe600;
    --card-back: #f4f4f4;
    --rule-light: #ffffff;
  }
  * { margin: 0; padding: 0; box-sizing: border-box; }
  html, body {
    width: 1200px; height: 1200px; overflow: hidden;
    background: var(--page);
  }
  .canvas { position: relative; width: 1200px; height: 1200px; }

  .band {
    position: absolute; left: 0; top: 775px;
    width: 1200px; height: 239px;
    background: var(--brand-blue);
  }

  .card {
    position: absolute; left: 283px;
    width: 641px; height: 356px;
    border-radius: 6px; overflow: hidden;
  }
  .card-front { top: 117px; background: var(--deep-navy); }
  .card-back { top: 606px; background: var(--card-back); }

  .front-panel {
    position: absolute; left: 0; top: 0;
    width: 150px; height: 100%;
    background: var(--brand-blue);
  }
  .front-rule {
    position: absolute; left: 160px; top: 0;
    width: 4px; height: 100%;
    background: var(--brand-blue);
  }

  .wordmark-dot {
    position: absolute; left: 45px; top: 128px;
    width: 60px; height: 60px; border-radius: 50%;
    background: var(--sun-yellow);
  }
  .wordmark {
    position: absolute; right: 99px; top: 124px;
    font-family: "Cinzel", "Copperplate", serif;
    font-weight: 400; font-size: 40px; line-height: 60px;
    color: var(--sun-yellow);
    text-align: right;
    letter-spacing: 1px;
  }

  .back-rule {
    position: absolute; left: 196px; right: 24px; bottom: 22px;
    height: 3px; background: var(--rule-light);
  }

  .portrait {
    position: absolute; left: 34px; top: 26px;
    width: 149px; height: 302px;
    background: linear-gradient(180deg, #e6e6e6 0%, #d9d2cc 30%, #e7c9d2 48%, #3a4f8c 62%, #2c3f78 88%, #f4f4f4 100%);
  }

  .back-text {
    position: absolute; left: 183px; right: 14px; top: 0;
    color: var(--brand-blue);
    font-family: "Gelasio", Georgia, serif;
  }
  .company-line {
    position: absolute; left: 0; top: 24px; white-space: nowrap;
    font-family: "Cinzel", "Copperplate", serif;
    font-size: 27px; letter-spacing: 0.3px;
  }
  .agent-name {
    position: absolute; left: 0; width: 434px; top: 80px; text-align: center;
    font-weight: 700; font-size: 47px; line-height: 56px;
  }
  .agent-title {
    position: absolute; left: 0; width: 434px; top: 138px; text-align: center;
    font-size: 34px; line-height: 40px;
  }
  .contact {
    position: absolute; left: 0; width: 434px; top: 210px; text-align: center;
    font-size: 19px; line-height: 26px;
    font-variant-numeric: oldstyle-nums;
  }
  .contact .gap { display: block; height: 3px; }
  .contact .tight { line-height: 22px; display: block; }
</style>
</head>
<body>
<main class="canvas">
  <div class="band"></div>

  <section class="card card-front" aria-label="Card front">
    <div class="front-panel"></div>
    <div class="front-rule"></div>
    <div class="wordmark-dot"></div>
    <div class="wordmark">Marigold Shore<br>Realty Inc</div>
  </section>

  <section class="card card-back" aria-label="Card back">
    <div class="back-rule"></div>
    <div class="portrait" role="img" aria-label="Portrait photo of Tim Harlow, broker and owner"></div>
    <div class="back-text">
      <p class="company-line">Marigold Shore Realty Inc</p>
      <h1 class="agent-name">Tim Harlow</h1>
      <p class="agent-title">Broker/Owner</p>
      <p class="contact">
        738 West Penrick Ave, Suite 400/500<br>
        Fort Lauderdale, FL 33315
        <span class="gap"></span>
        <span class="tight">954-327-8846 Direct</span>
        <span class="tight">timshomes@quillmail.net</span>
        <span class="tight">Website: StayPenrickAv.net</span>
      </p>
    </div>
  </section>
</main>
</body>
</html>
```